Young Accounting firm needing a captivating business card

We need a business card design that forces the person to look at the card because its either gold foil, plastic, or lettering pop up etc. We already have a logo with a specific gold color and we need to make it pop. We are an accounting firm. I need the words" accounting, payroll, licenses, audits, taxes" somewhere on the business card so as to describe what we do- preferably on the side where the logo is at.

Industry/Entity Type

Accounting

Contact Information for Business Card

Address 48276 9th Ave S Ste 305, Federal Way, WA 98117
Business Phone (360)418-2096
Fax (360)418-2157
Office Cell Phone (360)586-7319

Font styles to use
Serif

Colors
85abd2

Requirements
Must have
• It should state
• "Accounting" "Taxes" "Audits" "Licenses" "Payroll"
Nice to have
• Matte with gold foil, different textures, With Either a textured ivory background or gray blue slate background
Should not have
• colorful colors

```html
<!DOCTYPE html>
<html lang="en">
<head>
<meta charset="utf-8">
<title>Business Card – Back</title>
<link href="https://fonts.googleapis.com/css2?family=Source+Serif+4:opsz,wght@8..60,400;8..60,700&display=swap" rel="stylesheet">
<style>
  :root {
    --navy: #0c2b6e;
    --slate: #46659f;
    --gold: #c9a44c;
    --white: #ffffff;
  }
  html, body {
    margin: 0;
    padding: 0;
    width: 1200px;
    height: 686px;
    overflow: hidden;
    background: var(--navy);
  }
  .card {
    position: relative;
    width: 1200px;
    height: 686px;
    background: var(--navy);
    color: var(--white);
    font-family: "Source Serif 4", Georgia, serif;
    overflow: hidden;
  }
  .brand-mark {
    position: absolute;
    top: 48px;
    right: 40px;
    display: flex;
    align-items: center;
    gap: 16px;
    color: var(--slate);
    font-weight: 700;
    font-size: 42px;
    line-height: 1;
    letter-spacing: 1px;
  }
  .brand-square {
    width: 40px;
    height: 40px;
    background: var(--gold);
  }
  .identity {
    position: absolute;
    left: 80px;
    top: 58px;
    margin: 0;
    font-weight: 700;
    font-size: 60px;
    line-height: 80px;
  }
  .identity span { display: block; }
  .contact {
    position: absolute;
    left: 0;
    top: 282px;
    margin: 0;
    display: grid;
    grid-template-columns: 286px 57px auto;
    font-size: 40px;
    line-height: 57px;
  }
  .contact dt {
    grid-column: 1;
    text-align: right;
    font-weight: 700;
  }
  .contact .bar {
    grid-column: 2;
    padding-left: 12px;
    font-weight: 700;
    color: var(--gold);
  }
  .contact dd {
    grid-column: 3;
    margin: 0;
    font-weight: 400;
    white-space: nowrap;
  }
  .services {
    position: absolute;
    right: 40px;
    bottom: 44px;
    margin: 0;
    padding: 18px 0 0;
    list-style: none;
    border-top: 2px solid var(--gold);
    text-align: right;
    color: var(--gold);
    font-size: 26px;
    line-height: 40px;
    font-weight: 700;
    letter-spacing: 2px;
    text-transform: uppercase;
  }
</style>
</head>
<body>
  <div class="card">
    <div class="brand-mark">
      <div class="brand-square"></div>
      <span>LEDGERWAY</span>
    </div>

    <h1 class="identity">
      <span class="full-name">Full Name</span>
      <span class="job-title">Job Title</span>
    </h1>

    <dl class="contact">
      <dt>Address</dt><span class="bar">|</span>
      <dd>48276 9th Ave S Ste 305,<br>Federal Way, WA 98117</dd>
      <dt>Phone</dt><span class="bar">|</span>
      <dd>(360)418-2096</dd>
      <dt>Fax</dt><span class="bar">|</span>
      <dd>(360)418-2157</dd>
      <dt>Cell Phone</dt><span class="bar">|</span>
      <dd>(360)586-7319</dd>
      <dt>Email</dt><span class="bar">|</span>
      <dd>hello@ledgerwaytax.com</dd>
    </dl>

    <ul class="services">
      <li>Accounting</li>
      <li>Taxes</li>
      <li>Audits</li>
      <li>Licenses</li>
      <li>Payroll</li>
    </ul>
  </div>
</body>
</html>
```